Screening Mammography flyer for patients

We need a flyer design to inform our patients of our Screening Mammography program (it's a screening Diagnostic Imaging test). Women aged 50-74 years old are eligible for this exam. We also have a convenient booking system, when a patient can call us directly. There's no doctor’s referral needed to sign up for the test.
We are also starting the RVC Scan Champion program, when select patients will help spread the word and save lives.
The flyer has to be done with a lot of pink color as it is a traditional color for Breast cancer materials, with consideration of the hospital's corporate colors (the brand book is attached).

Industry/Entity Type

Diagnostic Imaging

```html
<!DOCTYPE html>
<html lang="en">
<head>
<meta charset="utf-8">
<title>Screening Mammography Flyer</title>
<link rel="stylesheet" href="https://fonts.googleapis.com/css2?family=Oswald:wght@700&family=Open+Sans:wght@400;600;700;800&family=Montserrat:wght@600;700&display=swap">
<style>
  :root {
    --page-bg: #ece7e1;
    --paper: #ffffff;
    --magenta: #c93b8f;
    --magenta-light: #d75aa2;
    --magenta-deep: #b82a7f;
    --purple: #6a1283;
    --lilac: #9a68b8;
    --hot-pink: #e2197b;
    --green: #8dc63f;
    --green-dark: #5da130;
    --ink: #1e1e1e;
  }
  html, body {
    margin: 0;
    width: 1200px;
    height: 1200px;
    overflow: hidden;
    background: var(--page-bg);
  }
  .flyer {
    position: absolute;
    left: 204px;
    top: 40px;
    width: 792px;
    height: 1120px;
    box-shadow: 0 6px 18px rgba(0,0,0,0.25);
    background: var(--paper);
    overflow: hidden;
  }
  .flyer svg { display: block; }
  .sans { font-family: 'Open Sans', sans-serif; }
  .condensed { font-family: 'Oswald', sans-serif; }
  .brand { font-family: 'Montserrat', sans-serif; }
</style>
</head>
<body>
<main class="flyer">
  <svg viewBox="0 0 953 1347" width="792" height="1120" xmlns="http://www.w3.org/2000/svg">
    <defs>
      <linearGradient id="photoTone" x1="0" y1="0" x2="1" y2="1">
        <stop offset="0" stop-color="#9a9c86"/>
        <stop offset="0.45" stop-color="#c9b29a"/>
        <stop offset="1" stop-color="#8b7a66"/>
      </linearGradient>
      <radialGradient id="ribbonTone" cx="0.35" cy="0.6" r="0.6">
        <stop offset="0" stop-color="#f7b3d4"/>
        <stop offset="1" stop-color="#ea79b1"/>
      </radialGradient>
    </defs>

    <!-- hero photo area -->
    <polygon class="hero-photo" role="img" aria-label="Photo: three smiling senior women taking a selfie together"
      points="0,0 953,0 953,318 486,598 0,312" fill="url(#photoTone)"/>

    <!-- diagonal bands -->
    <polygon class="band-left" points="0,318 486,602 575,712 0,428" fill="var(--magenta)"/>
    <polygon class="band-right" points="486,602 953,322 953,438 480,722" fill="var(--magenta-deep)"/>
    <polygon class="band-right-light" points="486,602 575,712 480,722" fill="var(--magenta-light)"/>
    <polygon class="panel-purple" points="480,722 953,440 953,1022" fill="var(--purple)"/>

    <!-- badge -->
    <ellipse class="ribbon-area" role="img" aria-label="Pink breast cancer awareness ribbon"
      cx="748" cy="500" rx="150" ry="140" fill="url(#ribbonTone)"/>
    <circle class="badge" cx="773" cy="470" r="128" fill="var(--paper)" stroke="var(--hot-pink)" stroke-width="12"/>
    <g class="badge-text sans" fill="var(--hot-pink)" font-weight="800" text-anchor="middle">
      <text x="773" y="426" font-size="46">EARLY</text>
      <text x="773" y="452" font-size="26">DETECTION</text>
      <text x="790" y="492" font-size="46">SAVES</text>
      <text x="797" y="531" font-size="46">LIVES</text>
    </g>

    <!-- program message -->
    <g class="program sans" fill="var(--paper)" text-anchor="end">
      <text x="922" y="672" font-size="28" font-weight="700">JOIN THE</text>
      <text x="922" y="718" font-size="44" font-weight="800">RVC SCAN</text>
      <text x="922" y="746" font-size="27" font-weight="400">CHAMPION PROGRAM</text>
      <text x="922" y="786" font-size="40" font-weight="800">TO HELP</text>
      <text x="922" y="824" font-size="40" font-weight="800">SAVE LIVES!</text>
    </g>

    <!-- hospital name -->
    <g class="hospital-name brand">
      <rect x="46" y="660" width="40" height="40" fill="var(--green)"/>
      <text x="100" y="672" font-size="22" font-weight="700" fill="#3a3a3a">RIVERVIEW</text>
      <text x="100" y="696" font-size="22" font-weight="700" fill="#3a3a3a">CREST</text>
      <text x="100" y="720" font-size="22" font-weight="700" fill="#3a3a3a">HOSPITAL</text>
      <line x1="46" y1="732" x2="370" y2="732" stroke="var(--green)" stroke-width="2"/>
      <text x="46" y="756" font-size="16" font-weight="600" fill="var(--green-dark)" letter-spacing="1">EASTVALE HEALTH NETWORK</text>
    </g>

    <!-- headline -->
    <text class="headline condensed" x="320" y="868" font-size="88" font-weight="700" fill="var(--purple)" text-anchor="middle" textLength="510">JUST BOOK IT</text>
    <line x1="67" y1="885" x2="575" y2="885" stroke="var(--purple)" stroke-width="1.5"/>
    <text class="audience sans" x="320" y="917" font-size="25" font-weight="600" fill="var(--magenta)" text-anchor="middle">For Women Aged 50-74</text>
    <line x1="67" y1="930" x2="575" y2="930" stroke="var(--purple)" stroke-width="1.5"/>

    <g class="referral sans" font-size="24" font-weight="800" text-anchor="middle" fill="var(--ink)">
      <text x="320" y="972">NO <tspan fill="var(--lilac)">DOCTER’S REFFERAL</tspan> NEEDED</text>
      <text x="320" y="1008">FOR YOUR <tspan fill="var(--lilac)">SCREENING MAMOGRAM</tspan></text>
    </g>

    <g class="booking sans" text-anchor="middle">
      <text x="320" y="1058" font-size="22" font-weight="600" fill="var(--ink)">To Book An Appointment</text>
      <text x="320" y="1098" font-size="34" font-weight="800" fill="var(--purple)">Call 555-010-4820 Ext.2150</text>
      <rect x="122" y="1108" width="421" height="30" rx="15" fill="var(--green)"/>
      <text x="332" y="1130" font-size="18" font-weight="700" fill="var(--paper)">Same Date Appoinments Available!</text>
    </g>

    <!-- date / time -->
    <g class="schedule sans" font-size="24" fill="var(--ink)">
      <text x="660" y="1062">Date:</text>
      <line x1="730" y1="1062" x2="893" y2="1062" stroke="var(--ink)" stroke-width="1.5"/>
      <text x="660" y="1138">Time:</text>
      <line x1="730" y1="1138" x2="893" y2="1138" stroke="var(--ink)" stroke-width="1.5"/>
    </g>

    <!-- footer -->
    <polygon class="footer-band" points="0,1157 352,1253 953,1157 953,1347 0,1347" fill="var(--magenta)"/>
    <polygon class="footer-shade" points="0,1157 352,1253 0,1310" fill="var(--magenta-deep)"/>
    <polygon class="footer-light" points="0,1310 352,1253 953,1160 953,1200 500,1347 0,1347" fill="var(--magenta-light)" opacity="0.5"/>

    <g class="contact sans" fill="var(--paper)">
      <text x="928" y="1258" font-size="19" font-weight="700" text-anchor="end">Diagnostic imaging @ Riverview Crest Hospital:</text>
      <line x1="478" y1="1268" x2="928" y2="1268" stroke="var(--paper)" stroke-width="1.5"/>
      <line x1="663" y1="1280" x2="663" y2="1336" stroke="var(--paper)" stroke-width="1.5"/>

      <g class="icon-pin">
        <circle cx="487" cy="1307" r="11" fill="none" stroke="var(--paper)" stroke-width="1.5"/>
        <path d="M487,1300 a4.5,4.5 0 0 1 4.5,4.5 c0,3.5 -4.5,8 -4.5,8 c0,0 -4.5,-4.5 -4.5,-8 a4.5,4.5 0 0 1 4.5,-4.5z" fill="var(--paper)"/>
      </g>
      <text x="508" y="1314" font-size="18">410 Harbour Ave.</text>

      <g class="icon-mail">
        <circle cx="685" cy="1291" r="11" fill="none" stroke="var(--paper)" stroke-width="1.5"/>
        <rect x="678" y="1286" width="14" height="10" fill="none" stroke="var(--paper)" stroke-width="1.3"/>
        <polyline points="678,1286 685,1292 692,1286" fill="none" stroke="var(--paper)" stroke-width="1.3"/>
      </g>
      <text x="926" y="1297" font-size="17" text-anchor="end">imaging@evhn.example</text>

      <g class="icon-web" fill="none" stroke="var(--paper)" stroke-width="1.3">
        <circle cx="685" cy="1323" r="11" stroke-width="1.5"/>
        <circle cx="685" cy="1323" r="6"/>
        <line x1="679" y1="1323" x2="691" y2="1323"/>
        <ellipse cx="685" cy="1323" rx="2.5" ry="6"/>
      </g>
      <text x="926" y="1329" font-size="17" text-anchor="end">www.evhn.example/imaging</text>
    </g>
  </svg>
</main>
</body>
</html>
```